Lumora Dwellings

Design a stylish Business card- we would like a businness card design that suits plastic business cards. Our card needs to show that we are tech savy and technology based so the design is crucial.

Target Market(s)

22-40

Industry/Entity Type

Plastic

Requirements
Must have
• attached is our logo. also double sided card would be nice.
my details

Tobias Fenwright
Director
0471596234
www.lumoradwellings.com.au
17 Ashcombe Lane, West Perth

```html
<!DOCTYPE html>
<html lang="en">
<head>
<meta charset="utf-8">
<title>Lumora Dwellings – Business Cards</title>
<link href="https://fonts.googleapis.com/css2?family=Questrial&display=swap" rel="stylesheet">
<style>
  :root {
    --page-bg: #eeeeee;
    --card-dark-center: #3b3b3b;
    --card-dark-edge: #050505;
    --card-blue-center: #22c4f4;
    --card-blue-edge: #1f68ad;
    --accent-blue: #2aa9e0;
    --light-text: #ffffff;
    --soft-text: #d8d8d8;
  }
  html, body {
    margin: 0;
    padding: 0;
    width: 1200px;
    height: 1069px;
    overflow: hidden;
    background: var(--page-bg);
    font-family: "Questrial", sans-serif;
  }
  .canvas {
    position: relative;
    width: 1200px;
    height: 1069px;
  }
  .card {
    position: absolute;
    width: 420px;
    height: 229px;
    border-radius: 16px;
    overflow: hidden;
    box-sizing: border-box;
  }
  .card--dark {
    background: radial-gradient(ellipse at 50% 45%, var(--card-dark-center) 0%, var(--card-dark-edge) 75%);
  }
  .card--blue {
    background: radial-gradient(ellipse at 40% 35%, var(--card-blue-center) 0%, var(--card-blue-edge) 85%);
  }
  .card--front-top { left: 94px; top: 181px; }
  .card--back-top { left: 654px; top: 181px; }
  .card--front-bottom { left: 111px; top: 680px; }
  .card--back-bottom { left: 670px; top: 681px; }

  /* Front brand block */
  .brand {
    position: absolute;
    left: 0; right: 0;
    top: 96px;
    text-align: center;
  }
  .brand__row {
    display: inline-flex;
    align-items: center;
    gap: 10px;
  }
  .brand__mark {
    width: 22px;
    height: 22px;
    background: var(--accent-blue);
  }
  .brand__name {
    color: var(--accent-blue);
    font-size: 27px;
    letter-spacing: 1px;
  }

  /* Back small brand */
  .brand-small {
    position: absolute;
    right: 22px;
    top: 30px;
    text-align: right;
  }
  .brand-small__row {
    display: inline-flex;
    align-items: center;
    gap: 5px;
  }
  .brand-small__mark {
    width: 10px;
    height: 10px;
    background: var(--accent-blue);
  }
  .brand-small__name {
    color: var(--accent-blue);
    font-size: 13px;
  }
  .card--blue .brand-small__mark { background: var(--light-text); }
  .card--blue .brand-small__name { color: var(--light-text); }

  .person {
    position: absolute;
    left: 27px;
    top: 84px;
    text-align: right;
  }
  .person__name {
    font-size: 18px;
    color: var(--accent-blue);
  }
  .person__role {
    font-size: 9px;
    color: var(--light-text);
    margin-top: 6px;
  }
  .card--blue .person__name { color: var(--light-text); }

  .contact {
    position: absolute;
    left: 212px;
    top: 133px;
    margin: 0;
    padding: 0;
    list-style: none;
    color: var(--light-text);
    font-size: 9.5px;
    line-height: 21px;
  }
  .website {
    position: absolute;
    left: 0; right: 0;
    bottom: 10px;
    text-align: center;
    font-size: 16px;
    letter-spacing: 1px;
    color: var(--accent-blue);
  }
  .card--blue .website { color: var(--light-text); }
</style>
</head>
<body>
<main class="canvas">

  <section class="card card--dark card--front-top" aria-label="Card front, dark">
    <div class="brand">
      <div class="brand__row">
        <span class="brand__mark"></span>
        <span class="brand__name">Lumora Dwellings</span>
      </div>
    </div>
  </section>

  <section class="card card--dark card--back-top" aria-label="Card back, dark">
    <div class="brand-small">
      <div class="brand-small__row">
        <span class="brand-small__mark"></span>
        <span class="brand-small__name">Lumora Dwellings</span>
      </div>
    </div>
    <div class="person">
      <div class="person__name">Tobias Fenwright</div>
      <div class="person__role">Director</div>
    </div>
    <ul class="contact">
      <li>A: 17 Ashcombe Lane, West Perth</li>
      <li>P: 0471596234</li>
      <li>E: hello@lumoradwellings.com.au</li>
    </ul>
    <div class="website">www.lumoradwellings.com.au</div>
  </section>

  <section class="card card--dark card--front-bottom" aria-label="Card front, dark">
    <div class="brand">
      <div class="brand__row">
        <span class="brand__mark"></span>
        <span class="brand__name">Lumora Dwellings</span>
      </div>
    </div>
  </section>

  <section class="card card--blue card--back-bottom" aria-label="Card back, blue">
    <div class="brand-small">
      <div class="brand-small__row">
        <span class="brand-small__mark"></span>
        <span class="brand-small__name">Lumora Dwellings</span>
      </div>
    </div>
    <div class="person">
      <div class="person__name">Tobias Fenwright</div>
      <div class="person__role">Director</div>
    </div>
    <ul class="contact">
      <li>A: 17 Ashcombe Lane, West Perth</li>
      <li>P: 0471596234</li>
      <li>E: hello@lumoradwellings.com.au</li>
    </ul>
    <div class="website">www.lumoradwellings.com.au</div>
  </section>

</main>
</body>
</html>
```